Business Card Design

Hoping for a black background business card, minimalistic design.
With the Marble Crest logo you created in white.

I would like to include:
My Name and title
Address (street address)
Reception: (phone number)
Fax: (fax number)
Reception: (email address)
Direct email: (email address)
Instagram: (ig handle)

```html
<!DOCTYPE html>
<html lang="en">
<head>
<meta charset="utf-8">
<title>Marble Crest Business Card</title>
<link href="https://fonts.googleapis.com/css2?family=Montserrat:wght@500&family=Open+Sans:wght@300;700&family=Poppins:wght@400&display=swap" rel="stylesheet">
<style>
  :root {
    --backdrop: #dedede;
    --band: #a0a09e;
    --card: #000000;
    --white: #ffffff;
    --muted: #d6d6d6;
    --accent: #5fc3c4;
    --rule: #7a7a7a;
    --seam: #1e1e1e;
  }
  * { margin: 0; padding: 0; box-sizing: border-box; }
  html, body { width: 1029px; height: 1200px; overflow: hidden; background: var(--backdrop); }
  .canvas { position: relative; width: 1029px; height: 1200px; overflow: hidden; }
  .band { position: absolute; inset: 0; }
  .card {
    position: absolute; left: 176px; width: 677px; height: 386px;
    background: var(--card); border-radius: 26px;
    box-shadow: 0 4px 12px rgba(0,0,0,0.35);
    overflow: hidden;
  }
  .card--front { top: 161px; }
  .card--back { top: 681px; }

  .logo { position: absolute; display: flex; align-items: center; color: var(--white); }
  .logo__mark { border: 3px solid var(--white); border-radius: 50%; flex: none; }
  .logo__rule { background: var(--white); width: 1.5px; flex: none; }
  .logo__name {
    font-family: "Montserrat", sans-serif; font-weight: 500;
    text-transform: uppercase; white-space: nowrap;
  }
  .card--front .logo { left: 158px; top: 154px; }
  .card--front .logo__mark { width: 84px; height: 84px; border-width: 4px; }
  .card--front .logo__rule { height: 84px; margin: 0 11px 0 12px; }
  .card--front .logo__name { font-size: 30px; letter-spacing: 2.6px; }

  .card--back .logo { left: 67px; top: 159px; }
  .card--back .logo__mark { width: 52px; height: 52px; }
  .card--back .logo__rule { height: 52px; margin: 0 7px 0 7px; }
  .card--back .logo__name { font-size: 18px; letter-spacing: 1.6px; }

  .seam { position: absolute; left: 0; right: 0; top: 166px; height: 1px; background: var(--seam); }
  .divider { position: absolute; left: 338px; top: 46px; width: 2.5px; height: 304px; background: var(--rule); }

  .person { position: absolute; left: 362px; top: 46px; color: var(--white); }
  .person__name { font-family: "Open Sans", sans-serif; font-size: 29px; font-weight: 300; line-height: 34px; }
  .person__name strong { font-weight: 700; }
  .person__title { font-family: "Poppins", sans-serif; font-size: 13px; color: var(--muted); margin-top: 2px; }

  .contact { position: absolute; left: 364px; display: flex; align-items: flex-start; gap: 9px; }
  .contact__icon {
    width: 27px; height: 24px; border: 2px solid var(--accent); flex: none;
    display: flex; align-items: center; justify-content: center; margin-top: 2px;
  }
  .contact__icon svg { width: 15px; height: 15px; fill: var(--accent); }
  .contact__text {
    font-family: "Poppins", sans-serif; font-size: 15.5px; line-height: 21px; color: var(--white);
    white-space: nowrap;
  }
  .contact--phone { top: 132px; }
  .contact--email { top: 195px; }
  .contact--address { top: 257px; }
  .contact--social { top: 318px; }
</style>
</head>
<body>
<div class="canvas">
  <svg class="band" width="1029" height="1200" viewBox="0 0 1029 1200" aria-hidden="true">
    <polygon points="0,585 1029,169 1029,525 0,941" fill="var(--band)"/>
  </svg>

  <section class="card card--front">
    <div class="logo">
      <span class="logo__mark"></span>
      <span class="logo__rule"></span>
      <span class="logo__name">Marble Crest</span>
    </div>
  </section>

  <section class="card card--back">
    <div class="seam"></div>
    <div class="logo">
      <span class="logo__mark"></span>
      <span class="logo__rule"></span>
      <span class="logo__name">Marble Crest</span>
    </div>
    <div class="divider"></div>

    <div class="person">
      <h1 class="person__name">JORDAN <strong>HALE</strong></h1>
      <p class="person__title">GRAPHIC DESIGNER</p>
    </div>

    <div class="contact contact--phone">
      <span class="contact__icon"><svg viewBox="0 0 24 24"><path d="M6.6 10.8a15.1 15.1 0 0 0 6.6 6.6l2.2-2.2c.3-.3.7-.4 1-.2 1.1.4 2.3.6 3.6.6.6 0 1 .4 1 1V20c0 .6-.4 1-1 1A17 17 0 0 1 3 4c0-.6.4-1 1-1h3.5c.6 0 1 .4 1 1 0 1.3.2 2.5.6 3.6.1.3 0 .7-.2 1z"/></svg></span>
      <p class="contact__text">+01 555 0142 880<br>+01 555 0142 881</p>
    </div>
    <div class="contact contact--email">
      <span class="contact__icon"><svg viewBox="0 0 24 24"><path d="M2 5h20v14H2z M3.5 6.5 12 13l8.5-6.5" fill="none" stroke="var(--accent)" stroke-width="0"/><path d="M2 5h20v14H2V5zm2 1.8V17h16V6.8l-8 6.1-8-6.1zM5.2 6.5 12 11.6l6.8-5.1H5.2z"/></svg></span>
      <p class="contact__text">hello@marblecrest.com<br>studio@marblecrest.com</p>
    </div>
    <div class="contact contact--address">
      <span class="contact__icon"><svg viewBox="0 0 24 24"><path d="M12 3 2 12h3v8h5v-5h4v5h5v-8h3z"/></svg></span>
      <p class="contact__text">Your City Address<br>Street Location, State, Country</p>
    </div>
    <div class="contact contact--social">
      <span class="contact__icon"><svg viewBox="0 0 24 24"><rect x="4" y="4" width="16" height="16" rx="4" fill="none" stroke="var(--accent)" stroke-width="2"/><circle cx="12" cy="12" r="3.5" fill="none" stroke="var(--accent)" stroke-width="2"/></svg></span>
      <p class="contact__text">marblecrest.studio</p>
    </div>
  </section>
</div>
</body>
</html>
```